Imported Fine Wine E-commerce site

We need an e-commerce site built from scratch. We currently have a website however it is on Magento and would like a more user friendly platform. Not sure if its possible to use any of the information. We're looking for a mostly white clean design with some red to match the logo.

Target Market(s)

30+

Coding

Coded - Design and coding required

Number of Pages Required

5+ page

Colors
ec1f27

Requirements
Must have
• Categories 'Red/White/Bubbles/Mixed cases/Gifts/Wholesale'
'sort by' functions.
Contact us form
Filter by on left hand side, Variety, Price, Region
Mobile friendly
Must be on a platform that i can update and make changes to it myself

```html
<!DOCTYPE html>
<html lang="en">
<head>
<meta charset="UTF-8">
<title>Cepa Cellar — Fine Wine</title>
<link rel="stylesheet" href="https://fonts.googleapis.com/css2?family=Cinzel:wght@400;500&family=Montserrat:wght@400;500;600&display=swap">
<style>
  :root {
    --wine-red: #c8182c;
    --ink: #14131a;
    --white: #ffffff;
    --text-dark: #1d1d22;
    --hero-deep: #0e0d12;
    --hero-mid: #2a2420;
    --hero-warm: #5a4630;
  }
  * { margin: 0; padding: 0; box-sizing: border-box; }
  html, body { width: 1200px; height: 900px; overflow: hidden; background: var(--white); }
  body { font-family: "Montserrat", sans-serif; color: var(--text-dark); }

  .hero { position: relative; width: 1200px; height: 600px; overflow: hidden; }
  .hero-photo {
    position: absolute; inset: 0;
    background:
      radial-gradient(ellipse at 70% 25%, rgba(140,120,95,0.45), transparent 55%),
      radial-gradient(ellipse at 45% 85%, rgba(160,120,60,0.45), transparent 50%),
      linear-gradient(160deg, var(--hero-deep) 0%, var(--hero-mid) 55%, var(--hero-warm) 100%);
  }
  .hero-shade { position: absolute; inset: 0; background: rgba(10,10,14,0.35); }

  .site-header {
    position: absolute; top: 0; left: 0; right: 0;
    display: flex; justify-content: space-between; align-items: center;
    padding: 34px 60px 0 70px;
  }
  .brand { display: flex; align-items: center; gap: 10px; color: var(--white);
    font-family: "Cinzel", serif; font-size: 24px; font-weight: 500; letter-spacing: 1px; }
  .brand-dot { width: 10px; height: 10px; border-radius: 50%; background: var(--white); }
  .main-nav { display: flex; gap: 54px; }
  .main-nav a { color: var(--white); text-decoration: none; font-size: 11px; font-weight: 600; letter-spacing: 0.5px; }

  .hero-content { position: absolute; top: 200px; left: 0; right: 0; text-align: center; color: var(--white); }
  .hero-title { font-family: "Cinzel", serif; font-weight: 400; font-size: 62px; line-height: 1.22; letter-spacing: -1px; }
  .hero-title .accent { color: var(--wine-red); }
  .hero-lead { margin-top: 30px; font-size: 18px; font-weight: 500; }
  .order-btn {
    display: inline-block; margin-top: 40px; padding: 14px 40px;
    border: 2px solid var(--white); border-radius: 26px;
    color: var(--white); text-decoration: none; font-size: 11px; font-weight: 600; letter-spacing: 0.5px;
  }
  .scroll-cue { position: absolute; bottom: 26px; left: 50%; transform: translateX(-50%); }

  .featured { display: flex; gap: 80px; padding: 56px 70px 0; }
  .featured-head { width: 560px; }
  .eyebrow { font-family: "Cinzel", serif; font-size: 14px; color: var(--wine-red); }
  .featured-title { margin-top: 14px; font-family: "Cinzel", serif; font-weight: 400; font-size: 34px; line-height: 1.25; color: var(--ink); }
  .rule { margin-top: 24px; width: 120px; height: 2px; background: var(--wine-red); }
  .featured-text { width: 420px; padding-top: 64px; font-size: 15px; line-height: 1.75; }
</style>
</head>
<body>
  <section class="hero">
    <div class="hero-photo" role="img" aria-label="Photo of friends toasting with glasses of white wine over a wooden board with cheese and olives"></div>
    <div class="hero-shade"></div>

    <header class="site-header">
      <div class="brand"><span class="brand-dot"></span>Cepa Cellar</div>
      <nav class="main-nav">
        <a href="#">HOME</a>
        <a href="#">ABOUT</a>
        <a href="#">WINES</a>
        <a href="#">KITS</a>
        <a href="#">BEST SELLERS</a>
        <a href="#">CONTACT</a>
      </nav>
    </header>

    <div class="hero-content">
      <h1 class="hero-title">Enjoy good moments<br>with a <span class="accent">good wine</span></h1>
      <p class="hero-lead">We sell best wines to you enjoy the best moments with passion and love</p>
      <a class="order-btn" href="#">ORDER NOW</a>
    </div>

    <svg class="scroll-cue" width="16" height="26" viewBox="0 0 16 26" aria-hidden="true">
      <rect x="1" y="1" width="14" height="24" rx="7" fill="none" stroke="#ffffff" stroke-width="1.5"/>
      <line x1="8" y1="6" x2="8" y2="10" stroke="#ffffff" stroke-width="1.5" stroke-linecap="round"/>
    </svg>
  </section>

  <section class="featured">
    <div class="featured-head">
      <p class="eyebrow">Featured Collections</p>
      <h2 class="featured-title">The Extraordinary Wine<br>Collection of Cepa Cellar</h2>
      <div class="rule"></div>
    </div>
    <p class="featured-text">Praesent aliquet urna sapien, vestibulum maximus tellus rhoncus sed. Aliquam augue tortor, egestas vel sagittis quis, tempus ac arcu.</p>
  </section>
</body>
</html>
```